Quarrow financial services, is a financial company that provides consultancy, brokerage services, and funding.

we will be providing the clients with insights, knowledge and data with regards to the financial markets.

with the brokerage services we will try to find the suitable counterparts that provide them with the best investments that suits their needs and expected return.

Target Market(s)

financial institutions, Corporates, high-net worth individuals

Industry/Entity Type

Financial Service

Contact Information for Business Card

Font styles to use
Other font styles liked:
• applemyungjo

Colors
00a990
848484

Requirements
Must have
• the logo at the back
Nice to have
• Finesse
Should not have
• boldness

```html
<!DOCTYPE html>
<html lang="en">
<head>
<meta charset="utf-8">
<title>Quarrow Financial Services — Business Card</title>
<link rel="stylesheet" href="https://fonts.googleapis.com/css2?family=Nanum+Myeongjo:wght@400&family=Open+Sans:wght@400&display=swap">
<style>
  :root {
    --teal: #00a990;
    --teal-light: #00c4b0;
    --teal-deep: #009a84;
    --grey: #848484;
    --grey-light: #b8b8b8;
    --paper: #ffffff;
    --paper-shade: #eeeeee;
    --backdrop: #e6e6e4;
  }
  * { margin: 0; padding: 0; box-sizing: border-box; }
  html, body {
    width: 1200px;
    height: 1023px;
    overflow: hidden;
    background: var(--backdrop);
  }
  .canvas {
    position: relative;
    width: 1200px;
    height: 1023px;
  }
  .card {
    position: absolute;
    left: 340px;
    width: 520px;
    height: 300px;
    border-radius: 16px;
    overflow: hidden;
    box-shadow: 0 6px 18px rgba(0, 0, 0, 0.18);
  }
  .card-front { top: 170px; background: linear-gradient(135deg, var(--paper), var(--paper-shade)); }
  .card-back {
    top: 560px;
    background: radial-gradient(circle at 50% 45%, var(--teal-light), var(--teal) 60%, var(--teal-deep));
  }
  .front-shapes { position: absolute; inset: 0; }

  .wordmark {
    position: absolute;
    display: flex;
    align-items: center;
    gap: 10px;
    font-family: "Nanum Myeongjo", serif;
    font-weight: 400;
    white-space: nowrap;
  }
  .wordmark-square { width: 16px; height: 16px; flex: none; }
  .wordmark-text { display: flex; flex-direction: column; line-height: 1; }
  .wordmark-name { font-size: 26px; letter-spacing: 2px; }
  .wordmark-sub { font-size: 9px; letter-spacing: 3px; margin-top: 5px; text-transform: uppercase; }

  .card-front .wordmark { left: 222px; top: 50px; color: var(--grey); }
  .card-front .wordmark-square { background: var(--teal); }

  .card-back .wordmark { left: 50%; top: 50%; transform: translate(-50%, -50%); color: var(--paper); }
  .card-back .wordmark-name { font-size: 42px; letter-spacing: 5px; }
  .card-back .wordmark-sub { font-size: 13px; letter-spacing: 5px; margin-top: 7px; }
  .card-back .wordmark-square { width: 24px; height: 24px; background: var(--paper); }

  .person {
    position: absolute;
    left: 30px;
    top: 168px;
    font-family: "Open Sans", sans-serif;
    font-weight: 400;
  }
  .person-name { font-size: 24px; color: var(--grey); letter-spacing: 0.5px; line-height: 1.1; }
  .person-title { font-size: 11px; color: var(--teal); letter-spacing: 0.5px; }

  .contact {
    position: absolute;
    right: 34px;
    bottom: 22px;
    list-style: none;
    font-family: "Open Sans", sans-serif;
    font-size: 12px;
    color: var(--paper);
    letter-spacing: 0.6px;
    line-height: 17px;
  }
  .contact li { display: flex; align-items: center; gap: 6px; }
  .contact svg { width: 10px; height: 10px; flex: none; }
  .contact .indent { padding-left: 16px; }
</style>
</head>
<body>
<main class="canvas">

  <section class="card card-front" aria-label="Card front">
    <svg class="front-shapes" viewBox="0 0 520 300" preserveAspectRatio="none" aria-hidden="true">
      <path d="M490,0 C500,50 510,90 520,125 L520,0 Z" fill="var(--grey-light)"/>
      <path d="M0,300 L0,262 C250,250 450,170 490,0 L503,0 C494,60 492,115 520,150 L520,300 Z" fill="var(--teal)"/>
      <path d="M510,0 C511,30 514,60 520,82 L520,0 Z" fill="var(--grey)"/>
    </svg>

    <div class="wordmark">
      <span class="wordmark-square"></span>
      <span class="wordmark-text">
        <span class="wordmark-name">QUARROW</span>
        <span class="wordmark-sub">Financial Services</span>
      </span>
    </div>

    <div class="person">
      <p class="person-name">Your Name</p>
      <p class="person-title">Title</p>
    </div>

    <ul class="contact">
      <li>
        <svg viewBox="0 0 10 10"><circle cx="5" cy="5" r="4.3" fill="none" stroke="currentColor" stroke-width="1"/><path d="M3.4,3 L4.2,2.8 4.6,4 4,4.4 Q4.6,5.6 5.6,6 L6,5.4 7.2,5.8 7,6.6 Q4,6.8 3.4,3 Z" fill="currentColor"/></svg>
        88-123-54321
      </li>
      <li>
        <svg viewBox="0 0 10 10"><rect x="0.8" y="2" width="8.4" height="6" fill="none" stroke="currentColor" stroke-width="1"/><path d="M1,2.3 L5,5.4 9,2.3" fill="none" stroke="currentColor" stroke-width="1"/></svg>
        info@yourweb.com
      </li>
      <li>
        <svg viewBox="0 0 10 10"><path d="M5,9.5 C2,6 1.8,4.8 1.8,3.8 A3.2,3.2 0 0 1 8.2,3.8 C8.2,4.8 8,6 5,9.5 Z" fill="currentColor"/><circle cx="5" cy="3.8" r="1.2" fill="var(--teal)"/></svg>
        Your address line 1
      </li>
      <li class="indent">Your address line 2</li>
    </ul>
  </section>

  <section class="card card-back" aria-label="Card back">
    <div class="wordmark">
      <span class="wordmark-square"></span>
      <span class="wordmark-text">
        <span class="wordmark-name">QUARROW</span>
        <span class="wordmark-sub">Financial Services</span>
      </span>
    </div>
  </section>

</main>
</body>
</html>
```